wealth management firm, professional group, new model

we have a logo that works but we need a card, white background using our colors...clean look

our tag line if can be used in

Steady Counsel for Every Stage

```html
<!DOCTYPE html>
<html lang="en">
<head>
<meta charset="UTF-8">
<title>Hollis Crane Advisory – Business Card</title>
<link href="https://fonts.googleapis.com/css2?family=Lato:wght@400;700&display=swap" rel="stylesheet">
<style>
  :root {
    --navy: #1a2e50;
    --ink: #1b2d4f;
    --grey-text: #555b63;
    --card: #ffffff;
    --backdrop: #ebebeb;
    --light: #ffffff;
  }
  * { margin: 0; padding: 0; box-sizing: border-box; }
  html, body { width: 1200px; height: 1000px; overflow: hidden; }
  body {
    background: var(--backdrop);
    position: relative;
    font-family: "Lato", Arial, sans-serif;
    color: var(--ink);
  }
  .card {
    position: absolute;
    left: 254px;
    width: 692px;
    height: 395px;
    background: var(--card);
    border-radius: 18px;
    overflow: hidden;
  }
  .card--front { top: 78px; }
  .card--back { top: 526px; }

  .wave { position: absolute; inset: 0; width: 100%; height: 100%; }
  .wave path { fill: var(--navy); }

  .brand {
    position: absolute;
    text-align: center;
    font-weight: 400;
    color: var(--ink);
    white-space: nowrap;
  }
  .card--front .brand { left: 40px; width: 262px; top: 128px; font-size: 26px; line-height: 34px; }

  .person { position: absolute; left: 40px; width: 262px; top: 198px; text-align: center; }
  .person__name { font-size: 29px; font-weight: 700; color: var(--ink); line-height: 36px; }
  .person__title { font-size: 16px; color: var(--grey-text); margin-top: 1px; }

  .contact {
    position: absolute;
    right: 42px;
    top: 195px;
    list-style: none;
    color: var(--light);
    font-size: 16px;
    text-align: right;
  }
  .contact li { display: flex; justify-content: flex-end; align-items: center; gap: 10px; line-height: 24px; }
  .contact li.address { align-items: flex-start; line-height: 21px; margin-bottom: 8px; }
  .contact svg { width: 12px; height: 12px; flex: none; fill: var(--light); }
  .contact li.address svg { margin-top: 4px; }

  .card--back .brand { left: 0; width: 100%; top: 180px; font-size: 40px; line-height: 50px; }

  .tagline {
    position: absolute;
    left: 0; width: 100%;
    top: 340px;
    text-align: center;
    font-size: 18px;
    color: var(--ink);
  }
</style>
</head>
<body>

<section class="card card--front">
  <svg class="wave" viewBox="0 0 692 395" preserveAspectRatio="none" aria-hidden="true">
    <path d="M0,285 C80,318 165,338 255,312 C355,282 430,150 560,120 C620,108 660,140 692,160 L692,395 L0,395 Z"/>
  </svg>

  <p class="brand">Hollis Crane Advisory</p>

  <div class="person">
    <p class="person__name">DANIEL REEVE</p>
    <p class="person__title">Founder &amp; CEO</p>
  </div>

  <ul class="contact">
    <li class="address">
      <span>Street Address Here, City<br>State, Country, ZIP 123</span>
      <svg viewBox="0 0 12 12"><path d="M6 0a4.2 4.2 0 0 0-4.2 4.2C1.8 7.4 6 12 6 12s4.2-4.6 4.2-7.8A4.2 4.2 0 0 0 6 0zm0 6a1.8 1.8 0 1 1 0-3.6A1.8 1.8 0 0 1 6 6z"/></svg>
    </li>
    <li>
      <span>(123) 456-7890</span>
      <svg viewBox="0 0 12 12"><path d="M2.4 0.6l1.8 0.2 0.8 2.6-1.3 1a7 7 0 0 0 3 3l1-1.3 2.6 0.8 0.2 1.8c-0.3 1.6-1.8 2.4-3.4 1.8A10 10 0 0 1 0.6 4C0 2.4 0.8 0.9 2.4 0.6z"/></svg>
    </li>
    <li>
      <span>(123) 456-7890</span>
      <svg viewBox="0 0 12 12"><path d="M3 0h6a1 1 0 0 1 1 1v10a1 1 0 0 1-1 1H3a1 1 0 0 1-1-1V1a1 1 0 0 1 1-1zm0.6 1.5v8h4.8v-8zM6 10.2a0.6 0.6 0 1 0 0 1.2 0.6 0.6 0 0 0 0-1.2z"/></svg>
    </li>
    <li>
      <span>(123) 456-7890</span>
      <svg viewBox="0 0 12 12"><path d="M3 0h6v3H3zM1 4h10a1 1 0 0 1 1 1v4H9.5v3h-7V9H0V5a1 1 0 0 1 1-1zm2.5 4v3h5V8z"/></svg>
    </li>
    <li>
      <span>info@yourwebsitehere.com</span>
      <svg viewBox="0 0 12 12"><path d="M0 2h12v1L6 6.8 0 3zm0 2.4l6 3.8 6-3.8V10H0z"/></svg>
    </li>
    <li>
      <span>yourwebsitehere.com</span>
      <svg viewBox="0 0 12 12"><path d="M6 0a6 6 0 1 0 0 12A6 6 0 0 0 6 0zm0 1.2c0.8 0 1.6 1.6 1.8 3.6H4.2C4.4 2.8 5.2 1.2 6 1.2zM4.2 6h3.6C7.6 8.6 6.8 10.8 6 10.8S4.4 8.6 4.2 6zM1.3 6h1.7c0 1.6 0.4 3 0.9 4A4.8 4.8 0 0 1 1.3 6zm7.7 0h1.7a4.8 4.8 0 0 1-2.6 4c0.5-1 0.9-2.4 0.9-4zM1.3 4.8A4.8 4.8 0 0 1 3.9 2c-0.5 0.8-0.8 1.8-0.9 2.8zm7.7 0c-0.1-1-0.4-2-0.9-2.8a4.8 4.8 0 0 1 2.6 2.8z"/></svg>
    </li>
  </ul>
</section>

<section class="card card--back">
  <p class="brand">Hollis Crane Advisory</p>
  <p class="tagline">Steady Counsel for Every Stage</p>
</section>

</body>
</html>
```